Marketing company needs business card design

Our company (Bright Harbor Partners) need a business card design for a marketing company. The design should of course include the logo and business colors (orange and blue). I would like the design to be clean and professional. The business card is going to be a die cut card that is leaf shaped (I have uploaded the template for it). I would love to see a design that is professional but nothing too "corporate."
Updates

Hello everyone,

Just wanted to let you know that I have uploaded an AI and EPS version of the logo for your convenience.

Thank you!

~Miranda

Industry/Entity Type

Marketing

Requirements
Must have
• Must have the following contact info:

Bright Harbor Partners
2871 Cedar Hollow Rd B204
Fairhaven, CO 80534

555.614.3827

info@brightharborpartners-example.com

```html
<!DOCTYPE html>
<html lang="en">
<head>
<meta charset="utf-8">
<title>Bright Harbor Partners – Business Card</title>
<link rel="stylesheet" href="https://fonts.googleapis.com/css2?family=Arimo:ital,wght@0,400;0,700;1,400&display=swap">
<style>
  :root {
    --page-bg: #eceae6;
    --brand-blue: #1596d6;
    --brand-blue-deep: #0b76b3;
    --brand-blue-light: #35b0ea;
    --brand-orange: #f2a03d;
    --card-white: #ffffff;
    --text-light: #ffffff;
  }
  * { box-sizing: border-box; margin: 0; padding: 0; }
  html, body {
    width: 1200px;
    height: 1166px;
    overflow: hidden;
    background: var(--page-bg);
    font-family: "Arimo", Arial, sans-serif;
  }
  .canvas {
    position: relative;
    width: 1200px;
    height: 1166px;
  }
  .card {
    position: absolute;
    left: 183px;
    width: 843px;
    height: 485px;
    box-shadow: 0 10px 24px rgba(0,0,0,0.25);
  }
  /* Front: leaf shape, rounded top-right and bottom-left */
  .card-front {
    top: 67px;
    border-radius: 0 230px 0 230px;
    background: linear-gradient(180deg, var(--brand-blue) 0%, var(--brand-blue-deep) 100%);
    padding: 16px 16px 22px 16px;
  }
  .card-front-face {
    position: relative;
    width: 100%;
    height: 100%;
    background: var(--card-white);
    border-radius: 0 214px 0 214px;
  }
  .brand-lockup {
    position: absolute;
    left: 0;
    right: 0;
    top: 140px;
    display: flex;
    align-items: center;
    justify-content: center;
    gap: 14px;
  }
  .brand-dot {
    width: 20px;
    height: 20px;
    border-radius: 50%;
    background: var(--brand-orange);
    flex: none;
  }
  .brand-name {
    font-family: "Arimo", Arial, sans-serif;
    font-weight: 700;
    font-size: 30px;
    line-height: 34px;
    color: var(--brand-blue);
    text-align: left;
  }
  /* Back: leaf shape, rounded top-left and bottom-right */
  .card-back {
    top: 574px;
    border-radius: 230px 0 230px 0;
    background: radial-gradient(ellipse at 70% 20%, var(--brand-blue-light) 0%, var(--brand-blue) 45%, var(--brand-blue-deep) 100%);
  }
  .card-back-frame {
    position: absolute;
    inset: 12px;
    border: 2px solid rgba(255,255,255,0.18);
    border-radius: 218px 0 218px 0;
  }
  .contact-mark {
    position: absolute;
    left: 82px;
    top: 207px;
    width: 62px;
    height: 62px;
    border-radius: 50%;
    border: 3px solid var(--text-light);
  }
  .contact-block {
    position: absolute;
    left: 181px;
    top: 216px;
    color: var(--text-light);
    font-size: 20px;
    line-height: 24px;
  }
  .contact-address { font-weight: 400; }
  .contact-phone { font-weight: 700; margin-top: 8px; }
  .contact-email { font-style: italic; margin-top: 7px; }
</style>
</head>
<body>
  <main class="canvas">
    <section class="card card-front" aria-label="Business card front">
      <div class="card-front-face">
        <div class="brand-lockup">
          <span class="brand-dot"></span>
          <span class="brand-name">Bright Harbor<br>Partners</span>
        </div>
      </div>
    </section>

    <section class="card card-back" aria-label="Business card back">
      <div class="card-back-frame"></div>
      <span class="contact-mark"></span>
      <div class="contact-block">
        <p class="contact-address">2871 Cedar Hollow Rd B204<br>Fairhaven, CO 80534</p>
        <p class="contact-phone">555.614.3827</p>
        <p class="contact-email">info@brightharborpartners-example.com</p>
      </div>
    </section>
  </main>
</body>
</html>
```